Letterhead to Prospective Clients

Create a letterhead (word & canva) that I will use to send letters to prospective clients and also include the Coralwood Estate Partners Logo, My Contact Details and Interchangeable "Suburb". Use the same font and colour pallete

Maris Dulworth | "Suburb" Specialist - Redlands & Surrounds
Mobile: 0417 862 095
Email: MD@CoralwoodEstatePartners.com.au

```html
<!DOCTYPE html>
<html lang="en">
<head>
<meta charset="utf-8">
<title>Letterhead – Maris Dulworth</title>
<link href="https://fonts.googleapis.com/css2?family=Montserrat:wght@300;400&family=Poppins:wght@400;600&display=swap" rel="stylesheet">
<style>
  :root {
    --navy: #0f1b44;
    --ink: #1d1d24;
    --body: #5a5c66;
    --muted: #8f93a3;
    --accent: #c9a46a;
    --label: #8fb0cf;
    --paper: #ffffff;
    --backdrop: #e9e9eb;
  }
  * { box-sizing: border-box; margin: 0; padding: 0; }
  html, body { width: 1200px; height: 1200px; overflow: hidden; }
  body { background: var(--backdrop); font-family: "Poppins", sans-serif; }

  .letterhead {
    position: absolute; left: 190px; top: 20px;
    width: 820px; height: 1160px;
    background: var(--paper);
    box-shadow: 0 6px 24px rgba(0,0,0,0.12);
  }

  .agent-title {
    position: absolute; left: 56px; top: 150px;
    font-family: "Montserrat", sans-serif; font-weight: 300;
    color: var(--ink);
  }
  .agent-title .name { font-size: 38px; letter-spacing: 0.5px; line-height: 1.15; white-space: nowrap; }
  .agent-title .area { font-size: 23px; letter-spacing: 0.6px; margin-top: 4px; white-space: nowrap; }

  .contact-band {
    position: absolute; right: 0; top: 0;
    width: 340px; height: 130px;
    background: var(--navy); color: #fff;
    padding: 54px 20px 0 24px;
    font-family: "Montserrat", sans-serif; font-size: 12.5px; line-height: 1.9;
  }
  .contact-band .row { display: flex; align-items: center; gap: 10px; white-space: nowrap; }
  .contact-band svg { width: 13px; height: 13px; flex: none; }

  .letter {
    position: absolute; left: 120px; top: 300px; width: 570px;
    font-size: 13px; color: var(--body); line-height: 1.55;
  }
  .letter .to-label { color: var(--label); font-size: 12px; letter-spacing: 0.5px; }
  .letter .recipient { color: var(--ink); font-weight: 600; font-size: 13px; line-height: 1.45; }
  .letter .salutation { color: var(--ink); font-weight: 600; font-size: 14px; margin: 26px 0 12px; }
  .letter p { margin-bottom: 18px; }

  .sign-off { margin: 28px 0 0 180px; }
  .sign-off .regards { color: var(--ink); font-weight: 600; font-size: 14px; }
  .sign-off .signature {
    width: 130px; height: 80px; margin: 8px 0 10px 20px;
    background: linear-gradient(135deg, #f4f4f6, #e4e4e8); border-radius: 6px;
  }
  .sign-off .signer { color: var(--ink); font-weight: 600; font-size: 14px; margin-left: 60px; line-height: 1.4; }
  .sign-off .role { color: var(--muted); font-size: 13px; margin-left: 60px; line-height: 1.4; }

  .brand-mark {
    position: absolute; right: 70px; bottom: 78px;
    display: flex; align-items: center; gap: 12px;
    font-family: "Montserrat", sans-serif; font-weight: 300;
    font-size: 22px; letter-spacing: 2px; color: var(--muted);
  }
  .brand-mark .dot { width: 14px; height: 14px; border-radius: 50%; background: var(--muted); }

  .footer-rule {
    position: absolute; left: 0; right: 0; bottom: 48px;
    height: 3px; background: var(--navy);
  }
</style>
</head>
<body>
  <main class="letterhead">
    <header>
      <div class="contact-band">
        <div class="row">
          <svg viewBox="0 0 24 24" aria-hidden="true"><path fill="var(--accent)" d="M6.6 10.8a15 15 0 0 0 6.6 6.6l2.2-2.2a1 1 0 0 1 1-.25 11.4 11.4 0 0 0 3.6.57 1 1 0 0 1 1 1V20a1 1 0 0 1-1 1A17 17 0 0 1 3 4a1 1 0 0 1 1-1h3.5a1 1 0 0 1 1 1c0 1.25.2 2.45.57 3.6a1 1 0 0 1-.25 1z"/></svg>
          <span>0417 862 095</span>
        </div>
        <div class="row">
          <svg viewBox="0 0 24 24" aria-hidden="true"><rect x="2" y="5" width="20" height="14" rx="1.5" fill="var(--accent)"/><path d="M3 6l9 7 9-7" fill="none" stroke="var(--navy)" stroke-width="1.6"/></svg>
          <span>MD@CoralwoodEstatePartners.com.au</span>
        </div>
      </div>
      <div class="agent-title">
        <div class="name">Maris Dulworth | "Suburb"</div>
        <div class="area">Specialist - Redlands &amp; Surrounds</div>
      </div>
    </header>

    <section class="letter">
      <div class="to-label">TO:</div>
      <div class="recipient">Arlen Pratcott<br>Hollis &amp; Vane / CEO</div>
      <div class="salutation">Dear Mr. Arlen Pratcott</div>
      <p>A letterhead is the heading at the top of a sheet of letter paper (stationery). That heading usually consists of a name and an address, and a logo or corporate design, and sometimes a background pattern. The term "letterhead" is often used to refer to the whole sheet imprinted with such a heading. Many companies and individuals prefer to create a letterhead template in a word processor or other software application.</p>
      <p>This generally includes the same information as pre-printed stationery but without the additional costs involved. Letterhead can then be printed on stationery (or plain paper) as needed on a local output device or sent electronically.</p>
      <p>This generally includes the same information as pre-printed stationery but without the additional costs involved. Letterhead can then be printed on stationery (or plain paper) as needed on a local output device or sent electronically.</p>
      <p>The term "letterhead" is often used to refer to the whole sheet imprinted with such a heading. Many companies and individuals prefer to create a letterhead template in a word processor or other software application.</p>

      <div class="sign-off">
        <div class="regards">Regards,</div>
        <div class="signature" role="img" aria-label="Handwritten signature"></div>
        <div class="signer">Tobias Renwick</div>
        <div class="role">General Manager</div>
      </div>
    </section>

    <footer>
      <div class="brand-mark"><span class="dot"></span><span>CORALWOOD ESTATE PARTNERS</span></div>
      <div class="footer-rule"></div>
    </footer>
  </main>
</body>
</html>
```